looking for sleek business card to standout from the crowd!

We are a young biotechnology company looking to help you personalize your health through understanding your genetic make up. We need you help in making a clean but sleek business card design using our new logo. The goal? Any time we give our cards out, people say "nice card!" The feel we are going for is "modern-techy". We don't want to come across as an old, giant pharma company, but not trying to be a hipster either.

Target Market(s)

healthcare and biotechnology industry.

Industry/Entity Type

Biotechnology

Contact Information for Business Card

Info to include on the card will be NAME, TITLE, EMAIL, PHONE. The companies website (www.corvalinbio.com) should also be on the card some where. Would like the logo, when printed, to be raised.

Requirements
Must have
• The logo we have attached in the color it is in. Fonts for text should lean toward more professional/tech.
Nice to have
• Prefer white/light color background
Should not have
• cartoons, landscape backgrounds images.

```html
<!DOCTYPE html>
<html lang="en">
<head>
<meta charset="utf-8">
<title>Corvalin business card</title>
<link href="https://fonts.googleapis.com/css2?family=Open+Sans:wght@400;600&display=swap" rel="stylesheet">
<style>
  :root {
    --backdrop: #e9e9e7;
    --card-white: #ffffff;
    --brand-blue: #1474bb;
    --text-grey: #3c3c3c;
    --emboss-blue: #1a7dc6;
  }
  * { margin: 0; padding: 0; box-sizing: border-box; }
  html, body {
    width: 1200px; height: 1000px; overflow: hidden;
    background: var(--backdrop);
    font-family: "Open Sans", Arial, sans-serif;
  }
  .canvas { position: relative; width: 1200px; height: 1000px; }
  .card {
    position: absolute; left: 266px; width: 666px; height: 397px;
    box-shadow: 0 3px 8px rgba(0,0,0,.25);
  }
  .card-front { top: 74px; background: var(--card-white); }
  .card-back { top: 534px; background: var(--brand-blue); }

  .company-name {
    position: absolute; font-weight: 600; line-height: 1; letter-spacing: 1px;
    white-space: nowrap;
  }
  .card-front .company-name { left: 42px; top: 176px; font-size: 40px; color: var(--brand-blue); }
  .card-back .company-name { left: 50%; top: 50%; transform: translate(-50%, -50%); font-size: 58px; color: var(--emboss-blue); }

  .details { position: absolute; left: 395px; top: 96px; color: var(--text-grey); font-size: 16px; line-height: 25px; }
  .person-name { color: var(--brand-blue); font-size: 22px; font-weight: 600; line-height: 28px; letter-spacing: .3px; }
  .person-title { margin-bottom: 17px; }
  .address { margin-bottom: 8px; }
  .contact-line { display: flex; align-items: center; gap: 7px; line-height: 24.5px; }
  .contact-icon { width: 15px; height: 15px; fill: var(--brand-blue); flex: none; }
</style>
</head>
<body>
<main class="canvas">
  <section class="card card-front">
    <div class="company-name">CORVALIN</div>
    <div class="details">
      <div class="person-name">DANA WHITLOCK</div>
      <div class="person-title">Managing Director/CEO</div>
      <div class="address">418 Linden Park Road<br>Ashford, MD 20900</div>
      <div class="contact-line">
        <svg class="contact-icon" viewBox="0 0 16 16" aria-hidden="true"><path d="M2 6c0-2 3-3.5 6-3.5S14 4 14 6v1.2h-3V6H5v1.2H2z"/><path d="M4 8h8l1.5 5h-11z"/></svg>
        <span>+ 000 000 0000</span>
      </div>
      <div class="contact-line">
        <svg class="contact-icon" viewBox="0 0 16 16" aria-hidden="true"><path d="M1 4h14v1L8 9.5 1 5z"/><path d="M1 6.5l7 4.5 7-4.5V12H1z"/></svg>
        <span>info@corvalinbio.com</span>
      </div>
      <div class="contact-line">
        <svg class="contact-icon" viewBox="0 0 16 16" aria-hidden="true"><circle cx="8" cy="8" r="6.5" fill="none" stroke="#1474bb" stroke-width="1.6"/><path d="M5 4.5c1.5.5 2 1.5 1.5 2.5S4 8 4.5 9.5 6.5 11 7 13" fill="none" stroke="#1474bb" stroke-width="1.4"/><path d="M9 8l5 2-2 1 2 2-1 1-2-2-1 2z"/></svg>
        <span>www.corvalinbio.com</span>
      </div>
    </div>
  </section>
  <section class="card card-back">
    <div class="company-name">CORVALIN</div>
  </section>
</main>
</body>
</html>
```